Unternehmen für Ordnung und Sauberkeit am Arbeitsplatz und Produkte zur Produktionsoptimierung benötigt Visitenkarten und Briefpapier
Zielgruppe
Produkte für Ordnung und Sauberkeit am Arbeitsplatz, Organisation von Arbeitsplätzen, Produkte zur Vereinfachung von Arbeitsabläufen, Produkte zur Produktionsoptimierung unter dem Lean Gedanke, Schlagwort: "5S", nachhaltig, sauber
Aufgabenstellung
Wir sind auf der Suche nach Visitenkarten und Briefpapier für das Unternehmen ourKarto. Nachhaltig, Sauber usw.. Unser Firmenlogo finden Sie anbei.

```html
<!DOCTYPE html>
<html lang="de">
<head>
<meta charset="utf-8">
<title>ourKarto – Briefpapier und Kuvert</title>
<link rel="stylesheet" href="https://fonts.googleapis.com/css2?family=Source+Sans+3:wght@400;700&display=swap">
<style>
  :root {
    --green: #2aaa3a;
    --green-dark: #1f8a2e;
    --grey: #7d7d7d;
    --grey-text: #8a8a8a;
    --line: #b9b9b9;
    --paper: #ffffff;
    --crop: #555555;
  }
  html, body { margin: 0; padding: 0; overflow: hidden; background: #ffffff; }
  .stage { display: block; width: 1200px; height: 1000px; }
  .brand, .sheet-text { font-family: "Source Sans 3", sans-serif; }
  .brand { font-weight: 700; }
  .brand--green { fill: var(--green-dark); }
  .brand--grey { fill: var(--grey); }
  .small-text { font-family: "Source Sans 3", sans-serif; fill: var(--grey-text); font-size: 6.2px; }
  .address-text { font-family: "Source Sans 3", sans-serif; fill: #666; font-size: 6.8px; }
  .crop-mark { stroke: var(--crop); stroke-width: 0.6; }
  .crop-mark--dashed { stroke-dasharray: 4 5; }
  .sheet { fill: var(--paper); filter: url(#sheet-shadow); }
  .band-green { fill: var(--green); }
  .band-grey { fill: var(--grey); }
  .divider { stroke: #999; stroke-width: 0.7; }
  .icon-box { fill: var(--green); }
  .icon-glyph { fill: none; stroke: #fff; stroke-width: 0.9; }
  .envelope-edge { fill: var(--paper); stroke: var(--line); stroke-width: 0.8; }
  .window { fill: #fff; stroke: #c8c8c8; stroke-width: 1; filter: url(#window-inset); }
</style>
</head>
<body>
<svg class="stage" viewBox="0 0 1200 1000" xmlns="http://www.w3.org/2000/svg">
  <defs>
    <filter id="sheet-shadow" x="-5%" y="-5%" width="110%" height="110%">
      <feDropShadow dx="1.5" dy="1.5" stdDeviation="1.5" flood-color="#000" flood-opacity="0.25"/>
    </filter>
    <filter id="window-inset" x="-5%" y="-5%" width="110%" height="110%">
      <feDropShadow dx="-1" dy="-1" stdDeviation="1.2" flood-color="#000" flood-opacity="0.2"/>
    </filter>
  </defs>

  <!-- Letterhead -->
  <g class="letterhead">
    <g class="crop-marks">
      <line class="crop-mark" x1="96" y1="165" x2="96" y2="190"/>
      <line class="crop-mark" x1="516" y1="165" x2="516" y2="190"/>
      <line class="crop-mark" x1="96" y1="810" x2="96" y2="835"/>
      <line class="crop-mark" x1="516" y1="810" x2="516" y2="835"/>
      <line class="crop-mark" x1="58" y1="202" x2="83" y2="202"/>
      <line class="crop-mark" x1="529" y1="202" x2="554" y2="202"/>
      <line class="crop-mark" x1="58" y1="797" x2="83" y2="797"/>
      <line class="crop-mark" x1="529" y1="797" x2="554" y2="797"/>
      <line class="crop-mark" x1="88" y1="406" x2="109" y2="406"/>
      <line class="crop-mark" x1="88" y1="595" x2="109" y2="595"/>
    </g>

    <rect class="sheet" x="96" y="202" width="420" height="595"/>

    <polygon class="band-grey" points="96,202 371,202 361,213 96,213"/>
    <polygon class="band-green" points="376,202 516,202 516,213 366,213"/>

    <text class="brand brand--green" x="134" y="270" font-size="34">ourKarto</text>

    <g class="footer-bank">
      <text class="brand brand--green" x="123" y="769" font-size="12">ourKarto</text>
      <line class="divider" x1="189" y1="760" x2="189" y2="783"/>
      <text class="small-text" x="199" y="765">Sparkasse Talbachgau</text>
      <text class="small-text" x="199" y="773.5">BLZ 000 600 00</text>
      <text class="small-text" x="199" y="782">Kto 300000000</text>
      <line class="divider" x1="269" y1="760" x2="269" y2="783"/>
      <text class="small-text" x="278" y="769">IBAN: DE00123456780012345678</text>
      <text class="small-text" x="278" y="777.5">BIC: TALBDE2XXXX</text>
    </g>

    <g class="footer-contact">
      <line class="divider" x1="398" y1="694" x2="398" y2="786"/>
      <rect class="icon-box" x="404" y="694" width="11" height="11" rx="2"/>
      <path class="icon-glyph" d="M409.5,703 C407,700 407,697.5 409.5,697 C412,697.5 412,700 409.5,703 Z"/>
      <text class="brand brand--green" x="420" y="702.5" font-size="9.5">ourKarto</text>
      <text class="small-text" x="418.5" y="711.5">Lindenhofweg 12</text>
      <text class="small-text" x="418.5" y="720.5">95120 Talbach</text>

      <rect class="icon-box" x="404" y="726" width="11" height="10" rx="2"/>
      <path class="icon-glyph" d="M406.5,730 Q409.5,727.5 412.5,730 M407.5,733.5 H411.5 V731.5 H407.5 Z"/>
      <text class="small-text" x="417.5" y="733.5">03140 / 41802 7</text>

      <rect class="icon-box" x="404" y="739" width="11" height="10" rx="2"/>
      <rect class="icon-glyph" x="407" y="741" width="5" height="6"/>
      <text class="small-text" x="417.5" y="746">03140 / 41802 / 3 5</text>

      <rect class="icon-box" x="404" y="752" width="11" height="10" rx="2"/>
      <circle class="icon-glyph" cx="409.5" cy="757" r="3"/>
      <text class="small-text" x="417.5" y="759">post@ourkarto-werk.de</text>

      <rect class="icon-box" x="404" y="764" width="11" height="10" rx="2"/>
      <circle class="icon-glyph" cx="409.5" cy="769" r="3"/>
      <line class="icon-glyph" x1="406.5" y1="769" x2="412.5" y2="769"/>
      <text class="small-text" x="418.5" y="771.5">www.ourkarto-werk.de</text>
    </g>

    <polygon class="band-green" points="96,786 371,786 361,797 96,797"/>
    <polygon class="band-grey" points="376,786 516,786 516,797 366,797"/>
  </g>

  <!-- Envelope front -->
  <g class="envelope-front">
    <g class="crop-marks">
      <line class="crop-mark" x1="653" y1="216" x2="653" y2="241"/>
      <line class="crop-mark" x1="1103" y1="216" x2="1103" y2="241"/>
      <line class="crop-mark crop-mark--dashed" x1="615" y1="254" x2="641" y2="254"/>
      <line class="crop-mark crop-mark--dashed" x1="1117" y1="254" x2="1142" y2="254"/>
      <line class="crop-mark" x1="615" y1="485" x2="641" y2="485"/>
      <line class="crop-mark" x1="1117" y1="485" x2="1142" y2="485"/>
      <line class="crop-mark" x1="653" y1="497" x2="653" y2="522"/>
      <line class="crop-mark" x1="1103" y1="497" x2="1103" y2="522"/>
    </g>

    <path class="envelope-edge" d="M653,254 L675,190 Q677,183 684,183 L1072,183 Q1079,183 1081,190 L1103,254 Z"/>
    <text class="brand brand--grey" x="878" y="221" font-size="20" text-anchor="middle" transform="rotate(180 878 221)" dominant-baseline="middle">ourKarto</text>

    <rect class="sheet" x="653" y="254" width="450" height="231"/>

    <g class="sender">
      <circle cx="686" cy="284" r="4.2" fill="none" stroke="var(--grey)" stroke-width="1.3"/>
      <circle cx="686" cy="283.5" r="1.2" fill="var(--grey)"/>
      <text class="brand brand--green" x="695" y="287" font-size="9.5">ourKarto</text>
      <text class="small-text" x="695" y="295.5">Lindenhofweg 12</text>
      <text class="small-text" x="695" y="304.5">95120 Talbach</text>
    </g>

    <rect class="window" x="681" y="384" width="180" height="72" rx="9"/>
    <g class="recipient">
      <text class="address-text" x="716" y="406">Marlene Brückner</text>
      <text class="address-text" x="716" y="415.5">Am Mühlenbach 27</text>
      <text class="address-text" x="716" y="425">53760 Bergfelden</text>
      <text class="address-text" x="716" y="434.5">SCHWEIZ</text>
    </g>

    <text class="brand brand--green" x="944" y="426" font-size="32">ourKarto</text>

    <polygon class="band-grey" points="653,477 952,477 946,485 653,485"/>
    <polygon class="band-green" points="957,477 1103,477 1103,485 951,485"/>
  </g>

  <!-- Envelope back -->
  <g class="envelope-back">
    <g class="crop-marks">
      <line class="crop-mark" x1="653" y1="527" x2="653" y2="552"/>
      <line class="crop-mark" x1="1103" y1="527" x2="1103" y2="552"/>
      <line class="crop-mark crop-mark--dashed" x1="615" y1="566" x2="641" y2="566"/>
      <line class="crop-mark crop-mark--dashed" x1="1117" y1="566" x2="1142" y2="566"/>
      <line class="crop-mark" x1="615" y1="796" x2="641" y2="796"/>
      <line class="crop-mark" x1="1117" y1="796" x2="1142" y2="796"/>
      <line class="crop-mark" x1="653" y1="810" x2="653" y2="835"/>
      <line class="crop-mark" x1="1103" y1="810" x2="1103" y2="835"/>
    </g>

    <rect class="sheet" x="653" y="566" width="450" height="231"/>
    <path class="envelope-edge" d="M653,566 L675,630 Q677,637 684,637 L1072,637 Q1079,637 1081,630 L1103,566" style="filter:url(#sheet-shadow)"/>
    <text class="brand brand--grey" x="878" y="609" font-size="20" text-anchor="middle">ourKarto</text>
  </g>
</svg>
</body>
</html>
```